Redesign the content on our home page

Thanks for your designs thus far.

There have been a few requests for feedback, so I have mocked up another layout. I am happy with everything except the 6 boxes in the green square. This is the piece I need the perfect design for.
- What the boxes look like
- Icons to be used
- Colours
- etc

__________________________________________________________________

We have the basic layout for our homepage, the header and footer are done. Please see attached (Homepage)

Only design in PSD etc needed, no coding. Also, header and footer not needed either, only formatting and graphic design of home page content. See eps file for the information.

I need more information added to the homepage and displayed in an organised way and designed so it presents well.

Our slogan is "Travel Insurance made simple". Therefore the design needs to represent this by being a simple, clear and clean layout of information. Website visitors need to be able to access and digest the information fast and this is reliant on the design of the information.

Attached is a mock up with all of the information.

Please ask and questions you need to help with the design.

Target Market(s)

Mostly female, any age.

Industry/Entity Type

Travel

Number of Pages Required

1 page

Font styles to use
Other font styles liked:
• MetaPro

Colors
f37122
33a6d7
33b8a4
dbdbdb
606060

Requirements
Must have
• - Follow home page look and feel
• - Simple design
• - Fast for a visitor to digest the information
Nice to have
• Simple design. Webpage is responsive so elements should look good when scaled for mobile.
Should not have
• No new colours to be introduced then what is in the design already or selected below.
• No new fonts.

```html
<!DOCTYPE html>
<html lang="en">
<head>
<meta charset="utf-8">
<title>Breezeway Travel Insurance</title>
<link rel="stylesheet" href="https://fonts.googleapis.com/css2?family=Fira+Sans:wght@300;400;500;700&display=swap">
<style>
:root{
  --orange:#f37122;
  --orange-dark:#dc5e12;
  --orange-soft:#f89a5e;
  --blue:#33a6d7;
  --teal:#33b8a4;
  --grey-light:#dbdbdb;
  --grey-bg:#f1f1f1;
  --grey:#606060;
  --white:#ffffff;
}
*{box-sizing:border-box;margin:0;padding:0}
html,body{width:1200px;height:3156px;overflow:hidden}
body{font-family:"Fira Sans",Arial,sans-serif;color:var(--grey);background:var(--white);position:relative;font-size:14px;line-height:1.5}
section,header,footer{position:absolute;left:0;width:1200px}

/* header */
.site-header{top:0;height:80px;background:var(--white);display:flex;align-items:center;padding:0 140px}
.brand{display:flex;align-items:center;gap:8px;font-weight:700;font-size:26px;color:var(--orange)}
.brand-box{width:22px;height:22px;background:var(--orange)}
.brand-tag{font-size:10px;color:var(--grey);font-weight:400;margin-left:4px}
.nav{margin-left:auto;display:flex;gap:22px;font-size:13px;color:var(--orange);align-items:center}
.nav-phone{position:absolute;right:140px;top:8px;font-size:12px;color:var(--orange);font-weight:500}

/* hero */
.hero{top:80px;height:380px;background:var(--orange);overflow:hidden}
.hero-skyline{position:absolute;left:0;bottom:70px;width:1200px;height:120px;background:linear-gradient(to top,rgba(255,255,255,.12),rgba(255,255,255,0))}
.hero-figure{position:absolute;left:230px;top:60px;width:140px;height:260px;background:linear-gradient(#e8532a,#c7441b);border-radius:8px}
.hero-case{position:absolute;left:380px;top:230px;width:60px;height:80px;background:#c7441b;border-radius:6px}
.hero-form{position:absolute;left:470px;top:70px;width:500px;color:var(--white)}
.form-row{display:flex;align-items:center;gap:14px;font-size:34px;font-weight:300;margin-bottom:14px}
.form-select{width:230px;height:44px;background:var(--white);border-radius:4px;position:relative}
.form-select::after{content:"";position:absolute;right:14px;top:18px;border:7px solid transparent;border-top-color:var(--grey)}
.date-box{width:62px;height:58px;background:var(--white);border-radius:4px;overflow:hidden;text-align:center}
.date-box b{display:block;background:var(--blue);color:var(--white);font-size:11px;font-weight:500;line-height:18px}
.date-box span{display:block;color:var(--grey);font-size:24px;font-weight:400;line-height:38px}
.hero-btn{display:inline-block;margin-left:30px;background:var(--orange-dark);color:var(--white);font-size:13px;padding:10px 28px;border-radius:20px}
.hero-partner{margin:14px 0 0 120px;font-size:13px;font-weight:500;opacity:.9}
.hero-wave{position:absolute;left:0;bottom:0}

/* intro */
.intro{top:460px;height:90px;text-align:center}
.intro h1{font-size:38px;font-weight:500;color:var(--orange);padding-left:120px}
.intro p{width:640px;margin:6px auto 0;padding-left:120px;font-size:13px;box-sizing:content-box}

/* features */
.features{top:560px;height:380px;display:grid;grid-template-columns:repeat(3,230px);column-gap:40px;row-gap:34px;padding-left:330px}
.feature-head{display:flex;align-items:center;gap:10px;margin-bottom:8px}
.feature-icon{flex:none}
.feature h3{font-size:16px;font-weight:500;color:var(--orange)}
.feature p{font-size:12px;line-height:1.55}

/* award */
.award{top:950px;height:140px;text-align:center}
.award-band{position:absolute;top:30px;left:0;width:1200px;height:60px;background:var(--orange)}
.award-title{position:relative;top:-2px;font-size:17px;font-weight:700;color:var(--grey)}
.award-badge{position:absolute;left:540px;top:20px;width:120px;height:80px;background:var(--white);border-radius:40px;border:4px solid var(--orange-dark)}
.award-badge::after{content:"";position:absolute;left:24px;top:22px;width:64px;height:28px;background:var(--teal);border-radius:14px}
.award-labels{position:absolute;top:96px;left:0;width:1200px;display:flex;justify-content:center;gap:140px}
.award-labels span{background:var(--orange-dark);color:var(--white);font-size:13px;padding:6px 18px;border-radius:0 0 8px 8px}

/* confidence */
.confidence{top:1110px;height:360px;text-align:center}
.confidence h2{font-size:24px;font-weight:500;color:var(--orange)}
.confidence .lead{width:720px;margin:8px auto 0;font-size:12px}
.badges{display:flex;justify-content:center;gap:26px;margin-top:26px}
.badge-card{width:200px;height:230px;border:2px solid var(--grey-light);border-radius:100px 100px 60px 60px;padding:18px 16px;background:var(--white)}
.badge-mark{width:110px;height:110px;margin:0 auto 12px;border-radius:50%;background:var(--orange)}
.badge-mark.alt{background:var(--grey-light)}
.badge-card p{font-size:11px;line-height:1.45}

/* rating */
.rating{top:1480px;height:220px;background:var(--grey-bg);text-align:center;padding-top:34px}
.rating h2{font-size:22px;font-weight:500;color:var(--orange)}
.rating-pills{display:flex;justify-content:center;gap:12px;margin:16px 0 12px}
.pill{display:flex;align-items:center;gap:6px;background:var(--teal);color:var(--white);border-radius:22px;padding:8px 22px;font-size:16px;font-weight:700}
.rating p{font-size:14px;color:var(--grey)}
.rating p b{color:var(--orange);font-weight:500}

/* resources */
.resources{top:1730px;height:300px;display:flex;justify-content:center;gap:70px;text-align:center}
.resource{width:230px}
.resource-icon{width:80px;height:80px;border-radius:50%;background:var(--orange);margin:0 auto 12px;display:flex;align-items:center;justify-content:center}
.resource h3{font-size:15px;font-weight:500;color:var(--orange);margin-bottom:6px}
.resource p{font-size:12px}
.resource a{display:block;margin-top:8px;font-size:12px;color:var(--orange);text-decoration:none}

/* traveller illustration */
.traveller{top:2040px;height:150px}
.traveller-art{position:absolute;left:540px;top:0;width:130px;height:140px;background:linear-gradient(var(--orange),var(--orange-dark));border-radius:10px}

/* as seen on */
.seen{top:2230px;height:180px;text-align:center}
.seen h2{font-size:15px;font-weight:500;color:var(--grey)}
.seen-row{display:flex;justify-content:center;align-items:center;gap:60px;margin-top:40px}
.seen-mark{height:34px;background:var(--grey-light);border-radius:4px}

/* footer cta */
.footer-cta{top:2430px;height:190px;background:var(--orange);color:var(--white);display:flex;padding:30px 140px 0;gap:40px}
.footer-brand{width:180px;background:var(--white);height:90px;border-radius:4px;padding:16px}
.footer-brand .brand{font-size:24px}
.footer-brand small{display:block;margin-top:18px;font-size:11px;color:var(--orange);font-weight:500}
.cta-news{width:320px}
.cta h4{font-size:15px;font-weight:700}
.cta p{font-size:12px;margin-bottom:8px}
.cta-input{height:30px;background:var(--white);border-radius:3px;margin-bottom:6px;font-size:11px;color:#999;padding:6px 10px}
.cta-btn{display:inline-block;background:var(--orange-dark);padding:5px 22px;border-radius:3px;font-size:12px}
.cta-quote,.cta-claim{width:200px}
.cta-phone{display:flex;align-items:center;gap:6px;font-size:13px;font-weight:500;margin-top:6px}

/* footer links */
.footer-links{top:2640px;height:240px;display:flex;padding-left:330px;gap:90px}
.footer-col h5{font-size:13px;font-weight:700;color:var(--grey);margin-bottom:6px}
.footer-col li{list-style:none;font-size:11px;color:var(--orange);line-height:1.7}

/* legal */
.legal{top:2900px;height:256px;padding:0 220px;text-align:center;font-size:9px;color:#9a9a9a;line-height:1.6}
.legal-rule{height:1px;background:var(--grey-light);margin-bottom:16px}
</style>
</head>
<body>

<header class="site-header">
  <div class="brand"><span class="brand-box"></span>breezeway<span class="brand-tag">Travel Insurance</span></div>
  <div class="nav-phone">&#9742; 1300 555 014</div>
  <nav class="nav"><span>Travel Insurance</span><span>Why our cover</span><span>Your Policy</span><span>Blog</span><span>Help</span><span>Contact us</span></nav>
</header>

<section class="hero">
  <div class="hero-skyline" role="img" aria-label="Faint city skyline silhouette"></div>
  <div class="hero-figure" role="img" aria-label="Illustrated traveller waving beside luggage"></div>
  <div class="hero-case" role="img" aria-label="Illustrated suitcase"></div>
  <div class="hero-form">
    <div class="form-row">I'm travelling to <span class="form-select"></span></div>
    <div class="form-row" style="padding-left:70px">from <span class="date-box"><b>Sep</b><span>09</span></span> till <span class="date-box"><b>Month</b><span>?</span></span></div>
    <span class="hero-btn">I'm travelling to multiple places &#9656; Get a quote</span>
    <div class="hero-partner">Meridian Underwriting</div>
  </div>
  <svg class="hero-wave" width="1200" height="80" viewBox="0 0 1200 80"><path d="M0 60 Q300 10 600 40 T1200 30 V80 H0Z" fill="#fff"/></svg>
</section>

<section class="intro">
  <h1>Travel Insurance made simple</h1>
  <p>We think buying travel cover should be easy, so we have kept our policies clear and our prices fair, so you can pack and go.</p>
</section>

<section class="features">
  <div class="feature">
    <div class="feature-head"><svg class="feature-icon" width="34" height="34"><circle cx="17" cy="17" r="15" fill="none" stroke="#f37122" stroke-width="2"/><path d="M10 17l5 5 9-10" fill="none" stroke="#f37122" stroke-width="2.5"/></svg><h3>Fast &amp; Simple Online Quotes</h3></div>
    <p>Get a price in under a minute with just a few details. No long forms, no fuss, just clear cover you can buy in moments.</p>
  </div>
  <div class="feature">
    <div class="feature-head"><svg class="feature-icon" width="34" height="34"><circle cx="17" cy="17" r="15" fill="none" stroke="#f37122" stroke-width="2"/><path d="M17 8v9l6 4" fill="none" stroke="#f37122" stroke-width="2.5"/></svg><h3>24/7 Emergency Assistance</h3></div>
    <p>Our support team is on call day and night, wherever you are. One call gets you help, advice and care when it counts most.</p>
  </div>
  <div class="feature">
    <div class="feature-head"><svg class="feature-icon" width="34" height="34"><circle cx="17" cy="17" r="15" fill="none" stroke="#f37122" stroke-width="2"/><path d="M11 24V14h12v10M14 14v-3h6v3" fill="none" stroke="#f37122" stroke-width="2"/></svg><h3>Multiple Trip Options</h3></div>
    <p>Single trip or yearly cover, it is your choice. Pick the plan that suits how often you go and only pay for what you need.</p>
  </div>
  <div class="feature">
    <div class="feature-head"><svg class="feature-icon" width="34" height="34"><circle cx="17" cy="17" r="15" fill="none" stroke="#f37122" stroke-width="2"/><path d="M10 18h14M17 11v14" stroke="#f37122" stroke-width="2.5"/></svg><h3>Medical Cover Included</h3></div>
    <p>Unlimited overseas medical cover comes with our main plans, so an illness or accident abroad will not ruin your savings.</p>
  </div>
  <div class="feature">
    <div class="feature-head"><svg class="feature-icon" width="34" height="34"><circle cx="17" cy="17" r="15" fill="none" stroke="#f37122" stroke-width="2"/><path d="M17 9a6 6 0 0 1 6 6c0 5-6 11-6 11s-6-6-6-11a6 6 0 0 1 6-6z" fill="none" stroke="#f37122" stroke-width="2"/></svg><h3>Easy Claims</h3></div>
    <p>Lodge your claim online in a few steps and track it as it moves. We keep you updated and aim to settle claims quickly.</p>
  </div>
  <div class="feature">
    <div class="feature-head"><svg class="feature-icon" width="34" height="34"><circle cx="17" cy="17" r="15" fill="none" stroke="#f37122" stroke-width="2"/><path d="M11 17h12M18 12l5 5-5 5" fill="none" stroke="#f37122" stroke-width="2.5"/></svg><h3>Simple Online Service</h3></div>
    <p>Change dates, add travellers or print your policy any time from your account. Everything you need sits in one place.</p>
  </div>
</section>

<section class="award">
  <div class="award-title">Award Winning Travel Insurance</div>
  <div class="award-band"></div>
  <div class="award-badge" role="img" aria-label="Comparison site award badge"></div>
  <div class="award-labels"><span>&#9733; Best Value Comprehensive Cover</span><span>&#9733; Best Value Seniors Comprehensive Cover</span></div>
</section>

<section class="confidence">
  <h2>Travel with Confidence</h2>
  <p class="lead">We keep you covered from the moment you book until you are home again, with real people ready to help at every step of the way.</p>
  <div class="badges">
    <div class="badge-card"><div class="badge-mark" role="img" aria-label="Emergency assistance badge"></div><p>Help on hand around the clock from a team that knows travel and speaks your language.</p></div>
    <div class="badge-card"><div class="badge-mark alt" role="img" aria-label="Underwriter badge"></div><p>Policies backed by Meridian Underwriting, one of the largest insurers in the world.</p></div>
    <div class="badge-card"><div class="badge-mark" role="img" aria-label="Price promise badge"></div><p>Find a cheaper like for like quote and we will look to beat it.</p></div>
    <div class="badge-card"><div class="badge-mark" role="img" aria-label="Cooling off period badge"></div><p>Change your mind within the cooling off period and get a full refund, no questions asked.</p></div>
  </div>
</section>

<section class="rating">
  <h2>Breezeway Travel Insurance is rated</h2>
  <div class="rating-pills">
    <span class="pill">&#9733;&#9733;&#9733;&#9733;&#9733; 4.6</span>
    <span class="pill">421 reviews</span>
  </div>
  <p>on <b>ReviewHub</b> as at 1/9/14</p>
</section>

<section class="resources">
  <div class="resource">
    <div class="resource-icon"><svg width="40" height="40"><path d="M20 6l16 28H4z" fill="none" stroke="#fff" stroke-width="3"/><path d="M20 16v9M20 28v2" stroke="#fff" stroke-width="3"/></svg></div>
    <h3>Travel Alerts</h3>
    <p>Stay up to date with the latest warnings and news for the places you plan to visit.</p>
  </div>
  <div class="resource">
    <div class="resource-icon"><svg width="40" height="40"><path d="M20 6a9 9 0 0 1 9 9c0 8-9 18-9 18s-9-10-9-18a9 9 0 0 1 9-9z" fill="none" stroke="#fff" stroke-width="3"/><circle cx="20" cy="15" r="3" fill="#fff"/></svg></div>
    <h3>Travel Guides</h3>
    <p>Handy tips and checklists to help you plan, pack and travel safely wherever you go.</p>
  </div>
  <div class="resource">
    <div class="resource-icon"><svg width="40" height="40"><rect x="8" y="8" width="24" height="26" fill="none" stroke="#fff" stroke-width="3"/><path d="M13 16h14M13 22h14M13 28h9" stroke="#fff" stroke-width="2"/></svg></div>
    <h3>Travel Blog</h3>
    <p>Stories and ideas from our team and readers to spark your next trip away.</p>
    <a>Visit the blog &#8250;</a>
  </div>
</section>

<section class="traveller">
  <div class="traveller-art" role="img" aria-label="Illustrated traveller walking with suitcase"></div>
</section>

<section class="seen">
  <h2>As seen on</h2>
  <div class="seen-row">
    <span class="seen-mark" style="width:120px"></span>
    <span class="seen-mark" style="width:100px"></span>
    <span class="seen-mark" style="width:130px"></span>
    <span class="seen-mark" style="width:120px"></span>
    <span class="seen-mark" style="width:90px"></span>
  </div>
</section>

<footer class="footer-cta">
  <div class="footer-brand"><div class="brand"><span class="brand-box"></span>breezeway</div><small>Meridian Underwriting</small></div>
  <div class="cta cta-news">
    <h4>Want Good Tips &amp; Freebies?</h4>
    <p>Join our newsletter</p>
    <div class="cta-input">Your name</div>
    <div class="cta-input">Your email</div>
    <span class="cta-btn">Sign up</span>
  </div>
  <div class="cta cta-quote">
    <h4>Need a Quote?</h4>
    <p>Contact us</p>
    <div class="cta-phone"><svg width="14" height="14"><path d="M3 1l3 3-2 2c1 2 2 3 4 4l2-2 3 3-2 2C6 13 1 8 1 3z" fill="#fff"/></svg>1300 555 014</div>
  </div>
  <div class="cta cta-claim">
    <h4>Making a Claim?</h4>
    <p>Tap here</p>
    <div class="cta-phone"><svg width="14" height="14"><path d="M3 1l3 3-2 2c1 2 2 3 4 4l2-2 3 3-2 2C6 13 1 8 1 3z" fill="#fff"/></svg>1300 555 014</div>
    <p style="margin-top:6px">See claim contact details</p>
  </div>
</footer>

<section class="footer-links">
  <div class="footer-col"><h5>Cover</h5><ul><li>Comprehensive Cover</li><li>Basic Cover</li><li>Annual Multi Trip</li><li>Seniors Cover</li><li>Domestic Cover</li><li>Ski &amp; Snow Cover</li><li>Family Cover</li></ul></div>
  <div class="footer-col"><h5>Support</h5><ul><li>Help &amp; FAQs</li><li>Make a Claim</li><li>Policy Wording</li><li>Manage My Policy</li><li>Emergency Help</li><li>Contact Us</li></ul></div>
  <div class="footer-col"><h5>About</h5><ul><li>Why Breezeway</li><li>Our Team</li><li>Reviews</li><li>Privacy Policy</li><li>Terms of Use</li><li>Sitemap</li></ul></div>
</section>

<section class="legal">
  <div class="legal-rule"></div>
  <p>Breezeway Travel Insurance is issued by Meridian Underwriting. Any advice on this site is general and does not take into account your objectives, financial situation or needs. Please read the policy wording before you buy to decide if the cover is right for you. Cover is subject to the terms, conditions, limits and exclusions in the policy. All rights reserved.</p>
</section>

</body>
</html>
```